Bellwether Home Inspections

We need stationery for our new home inspection company. We inspect homes for people prior to purchasing to ensure the property is in good condition, as well as inspecting new homes to ensure they have been built to the appropriate standards. We are happy to look at combinations of colours. The use of a water mark would be good. Open to suggestions.

Industry/Entity Type

Home Inspection

```html
<!DOCTYPE html>
<html lang="en">
<head>
<meta charset="utf-8">
<title>Bellwether Home Inspections – Letterhead</title>
<link href="https://fonts.googleapis.com/css2?family=Titillium+Web:wght@400&family=Mr+Dafoe&display=swap" rel="stylesheet">
<style>
  :root{
    --bg:#f1f1f1;
    --paper:#ffffff;
    --brand-blue:#2f5f8a;
    --brand-grey:#7d7f83;
    --ink:#2a2a2a;
    --watermark:#ececec;
  }
  html,body{margin:0;padding:0;width:1200px;height:1000px;overflow:hidden;background:var(--bg);}
  .canvas{position:relative;width:1200px;height:1000px;}
  .sheet{position:absolute;top:192px;width:440px;height:616px;background:var(--paper);overflow:hidden;
    font-family:"Titillium Web",Arial,sans-serif;color:var(--ink);}
  .sheet--plain{left:130px;}
  .sheet--watermark{left:613px;}
  .brand{position:absolute;top:252px;left:0;width:100%;display:flex;justify-content:center;align-items:center;gap:7px;top:56px;}
  .brand__mark{width:12px;height:12px;background:var(--brand-blue);}
  .brand__name{font-size:13px;line-height:13px;color:var(--brand-blue);font-weight:400;text-align:left;}
  .salutation{position:absolute;left:58px;top:157px;font-size:8px;margin:0;}
  .body{position:absolute;left:72px;width:296px;font-size:7.3px;line-height:11px;text-align:justify;margin:0;hyphens:auto;}
  .body--first{top:176px;}
  .body--second{top:298px;}
  .signature{position:absolute;left:265px;top:420px;font-family:"Mr Dafoe",cursive;font-size:24px;color:#111;}
  .contact{position:absolute;left:0;width:100%;text-align:center;font-size:5.6px;line-height:9px;color:#444;}
  .contact--address{top:581px;}
  .contact--lines{top:590px;}
  .contact svg{width:6px;height:6px;vertical-align:-1px;fill:#555;margin:0 1px 0 3px;}
  .band{position:absolute;top:605px;height:9px;}
  .band--blue{left:0;width:317px;background:var(--brand-blue);}
  .band--grey{left:321px;width:119px;background:var(--brand-grey);}
  .watermark{position:absolute;left:144px;top:388px;width:296px;height:214px;background:var(--watermark);}
</style>
</head>
<body>
<div class="canvas">

  <section class="sheet sheet--plain">
    <div class="brand"><span class="brand__mark"></span><span class="brand__name">Bellwether<br>Home Inspections</span></div>
    <p class="salutation">Dear Client,</p>
    <p class="body body--first">Lorem ipsum dolor sit amet, consectetur adipiscing elit. Nulla sodales nisi vitae Lorem ipsum dolor sit amet, consectetur adipiscing elit. Suspendisse feugiat eros nisl, a facilisis risus eleifend sed. Aliquam mauris enim, fermentum eu lacinia sit amet, laoreet eu leo. Nullam eleifend nulla in libero tristique, ac vulputate odio tincidunt. Etiam non condimentum tortor. Integer suscipit neque nec odio porttitor cursus. Phasellus a sapien blandit, suscipit justo id, condimentum ante. Morbi tristique justo risus, id mattis dui molestie ut. Nullam volutpat ut quam commodo faucibus. Pellentesque urna est, interdum in elit quis, pharetra elementum orci. Nam pharetra velit molestie justo placerat scelerisque.</p>
    <p class="body body--second">Ut vitae interdum diam, in euismod ante. Pellentesque volutpat, risus sit amet sodales hendrerit, mi turpis vulputate dolor, eget cursus nulla eros nec tellus. Nulla tincidunt molestie libero vel pretium. Donec condimentum nulla sit amet risus semper imperdiet. Duis congue eros nec diam blandit, et pellentesque sapien auctor. Curabitur iaculis enim lectus, in imperdiet mauris mattis eget. Etiam ac ornare metus. Mauris risus leo, egestas at dolor a, ultrices adipiscing est. Nunc faucibus scelerisque mollis. Pellentesque aliquet mauris tellus, id dignissim risus viverra et. Mauris venenatis lobortis eros. Nam id diam in ligula malesuada feugiat. Cras turpis felis, aliquet id mauris elementum, feugiat ultricies nisl.</p>
    <div class="signature">Dana Whitlock</div>
    <div class="contact contact--address"><svg viewBox="0 0 10 10"><path d="M5 0a3.5 3.5 0 0 0-3.5 3.5C1.5 6 5 10 5 10s3.5-4 3.5-6.5A3.5 3.5 0 0 0 5 0zm0 5a1.5 1.5 0 1 1 0-3 1.5 1.5 0 0 1 0 3z"/></svg>48 Harbor Lane, Millbrook, 20415, Country</div>
    <div class="contact contact--lines"><svg viewBox="0 0 10 10"><path d="M2 0l2 2.5-1 1.5c.7 1.3 1.7 2.3 3 3l1.5-1L10 8l-1.5 2C4 10 0 6 0 1.5z"/></svg>555-0192-48 <svg viewBox="0 0 10 10"><rect x="0" y="3" width="10" height="6"/><rect x="2" y="0" width="6" height="3"/></svg>555-0192-48 <svg viewBox="0 0 10 10"><path d="M0 2h10v6H0zM0 2l5 3.5L10 2"/></svg>hello@bellwetherinspect.com <svg viewBox="0 0 10 10"><circle cx="5" cy="5" r="5"/></svg>www.bellwetherinspect.com</div>
    <div class="band band--blue"></div><div class="band band--grey"></div>
  </section>

  <section class="sheet sheet--watermark">
    <div class="watermark" role="img" aria-label="Faint brand watermark area"></div>
    <div class="brand"><span class="brand__mark"></span><span class="brand__name">Bellwether<br>Home Inspections</span></div>
    <p class="salutation">Dear Client,</p>
    <p class="body body--first">Lorem ipsum dolor sit amet, consectetur adipiscing elit. Nulla sodales nisi vitae Lorem ipsum dolor sit amet, consectetur adipiscing elit. Suspendisse feugiat eros nisl, a facilisis risus eleifend sed. Aliquam mauris enim, fermentum eu lacinia sit amet, laoreet eu leo. Nullam eleifend nulla in libero tristique, ac vulputate odio tincidunt. Etiam non condimentum tortor. Integer suscipit neque nec odio porttitor cursus. Phasellus a sapien blandit, suscipit justo id, condimentum ante. Morbi tristique justo risus, id mattis dui molestie ut. Nullam volutpat ut quam commodo faucibus. Pellentesque urna est, interdum in elit quis, pharetra elementum orci. Nam pharetra velit molestie justo placerat scelerisque.</p>
    <p class="body body--second">Ut vitae interdum diam, in euismod ante. Pellentesque volutpat, risus sit amet sodales hendrerit, mi turpis vulputate dolor, eget cursus nulla eros nec tellus. Nulla tincidunt molestie libero vel pretium. Donec condimentum nulla sit amet risus semper imperdiet. Duis congue eros nec diam blandit, et pellentesque sapien auctor. Curabitur iaculis enim lectus, in imperdiet mauris mattis eget. Etiam ac ornare metus. Mauris risus leo, egestas at dolor a, ultrices adipiscing est. Nunc faucibus scelerisque mollis. Pellentesque aliquet mauris tellus, id dignissim risus viverra et. Mauris venenatis lobortis eros. Nam id diam in ligula malesuada feugiat. Cras turpis felis, aliquet id mauris elementum, feugiat ultricies nisl.</p>
    <div class="signature">Dana Whitlock</div>
    <div class="contact contact--address"><svg viewBox="0 0 10 10"><path d="M5 0a3.5 3.5 0 0 0-3.5 3.5C1.5 6 5 10 5 10s3.5-4 3.5-6.5A3.5 3.5 0 0 0 5 0zm0 5a1.5 1.5 0 1 1 0-3 1.5 1.5 0 0 1 0 3z"/></svg>48 Harbor Lane, Millbrook, 20415, Country</div>
    <div class="contact contact--lines"><svg viewBox="0 0 10 10"><path d="M2 0l2 2.5-1 1.5c.7 1.3 1.7 2.3 3 3l1.5-1L10 8l-1.5 2C4 10 0 6 0 1.5z"/></svg>555-0192-48 <svg viewBox="0 0 10 10"><rect x="0" y="3" width="10" height="6"/><rect x="2" y="0" width="6" height="3"/></svg>555-0192-48 <svg viewBox="0 0 10 10"><path d="M0 2h10v6H0zM0 2l5 3.5L10 2"/></svg>hello@bellwetherinspect.com <svg viewBox="0 0 10 10"><circle cx="5" cy="5" r="5"/></svg>www.bellwetherinspect.com</div>
    <div class="band band--blue"></div><div class="band band--grey"></div>
  </section>

</div>
</body>
</html>
```